Livestock Consulting Company has a logo but needs business cards and a uniform logo

My company works with farmers advising them on managing cattle and sheep. I have a logo but need business cards and a version of my logo to go onto my work shirts. I need the following wording added to my logo for my shirts "Marlowby Livestock Consulting".

```html
<!DOCTYPE html>
<html lang="en">
<head>
<meta charset="utf-8">
<title>Marlowby Livestock Consulting – Business Card</title>
<link href="https://fonts.googleapis.com/css2?family=Montserrat:wght@500;600;800&display=swap" rel="stylesheet">
<style>
  :root {
    --bg: #1e1f24;
    --brown: #7a5f42;
    --brown-dark: #6a5139;
    --white: #ffffff;
    --ink: #3a2d20;
  }
  * { box-sizing: border-box; margin: 0; padding: 0; }
  html, body { width: 1200px; height: 800px; overflow: hidden; }
  body {
    background: var(--bg);
    font-family: "Montserrat", sans-serif;
    position: relative;
  }
  .card {
    position: absolute;
    top: 240px;
    width: 540px;
    height: 320px;
    border-radius: 26px;
    overflow: hidden;
  }
  .card-back {
    left: 40px;
    background: var(--brown);
  }
  .card-back .back-name {
    position: absolute;
    top: 176px;
    right: 40px;
    color: var(--white);
    font-weight: 800;
    font-size: 22px;
    letter-spacing: 0.5px;
  }
  .card-front {
    left: 620px;
    background: var(--white);
  }
  .brand {
    position: absolute;
    top: 78px;
    right: 44px;
    width: 230px;
    text-align: center;
    color: var(--brown);
    font-weight: 800;
    text-transform: uppercase;
    line-height: 1.15;
  }
  .brand-circle {
    display: block;
    width: 22px;
    height: 22px;
    border-radius: 50%;
    background: var(--brown);
    margin: 0 auto 12px;
  }
  .brand-name { font-size: 26px; display: block; }
  .brand-sub { font-size: 17px; display: block; letter-spacing: 0.5px; }
  .name-tab {
    position: absolute;
    left: 0;
    top: 112px;
    width: 236px;
    height: 84px;
    background: var(--brown);
    border-radius: 0 42px 42px 0;
    color: var(--white);
    padding: 18px 0 0 26px;
  }
  .person-name { font-weight: 800; font-size: 22px; letter-spacing: 0.5px; }
  .person-role { font-weight: 500; font-size: 14px; letter-spacing: 0.5px; margin-top: 2px; }
  .contacts {
    position: absolute;
    left: 26px;
    bottom: 30px;
    list-style: none;
    color: var(--ink);
    font-weight: 500;
    font-size: 14px;
  }
  .contacts li { display: flex; align-items: center; gap: 10px; margin-top: 8px; }
  .icon {
    width: 20px; height: 20px;
    border-radius: 50%;
    background: var(--brown);
    display: flex; align-items: center; justify-content: center;
    flex: none;
  }
</style>
</head>
<body>
  <div class="card card-back" role="img" aria-label="Card back: brown surface with subtle embossed pattern">
    <span class="back-name">Marlowby</span>
  </div>

  <div class="card card-front">
    <div class="brand">
      <span class="brand-circle"></span>
      <span class="brand-name">Marlowby Livestock</span>
      <span class="brand-sub">Consulting</span>
    </div>

    <div class="name-tab">
      <p class="person-name">DANIEL REYES</p>
      <p class="person-role">CEO/FOUNDER</p>
    </div>

    <ul class="contacts">
      <li>
        <span class="icon"><svg width="11" height="11" viewBox="0 0 24 24"><path fill="#fff" d="M6.6 10.8a15.1 15.1 0 0 0 6.6 6.6l2.2-2.2a1 1 0 0 1 1-.25 11.4 11.4 0 0 0 3.6.6 1 1 0 0 1 1 1V20a1 1 0 0 1-1 1A17 17 0 0 1 3 4a1 1 0 0 1 1-1h3.5a1 1 0 0 1 1 1c0 1.25.2 2.45.6 3.6a1 1 0 0 1-.25 1z"/></svg></span>
        555-014-2937
      </li>
      <li>
        <span class="icon"><svg width="11" height="11" viewBox="0 0 24 24"><path fill="#fff" d="M3 5h18v14H3zm2 2v.5l7 4.5 7-4.5V7l-7 4.5z"/></svg></span>
        dan@marlowbyconsulting.com
      </li>
      <li>
        <span class="icon"><svg width="11" height="11" viewBox="0 0 24 24" fill="none" stroke="#fff" stroke-width="2"><circle cx="12" cy="12" r="9"/><path d="M3 12h18M12 3c3 3 3 15 0 18M12 3c-3 3-3 15 0 18"/></svg></span>
        www.marlowbyconsulting.com
      </li>
    </ul>
  </div>
</body>
</html>
```